Business Card Designs

Looking to design a 3.5" x 2" standard business card for our employees.
The design needs to be sleek, simple, and modern. We would like our logo (attached) to be incorporated, but not in that colour, rather an outline of the logo in either gold or silver (whichever looks better).

Modern and Simple is what we are looking for, but be creative in incorporating the logo.

```html
<!DOCTYPE html>
<html lang="en">
<head>
<meta charset="utf-8">
<title>Harbourline Suites – Business Card</title>
<link rel="stylesheet" href="https://fonts.googleapis.com/css2?family=Barlow+Semi+Condensed:wght@400;600&family=Montserrat:wght@400;600&display=swap">
<style>
  :root {
    --backdrop: #4a3d2e;
    --card: #232323;
    --card-edge: #111111;
    --teal: #5fb3aa;
    --teal-muted: #5f9896;
    --ink: #ececec;
    --mark-grey: #6c6c6c;
    --silver: #a9a9a9;
    --shade: #0e0e0e;
  }
  * { margin: 0; padding: 0; box-sizing: border-box; }
  html, body {
    width: 900px; height: 1200px; overflow: hidden;
    background: var(--backdrop);
  }
  .canvas { position: relative; width: 900px; height: 1200px; }
  .card {
    position: absolute; left: 78px; width: 744px; height: 442px;
    background: var(--card); border-radius: 28px; overflow: hidden;
    box-shadow: 0 4px 0 var(--card-edge), 0 10px 24px rgba(0,0,0,.45);
  }
  .card--front { top: 130px; }
  .card--back { top: 638px; }

  .company {
    position: absolute; left: 35px; top: 64px;
    font-family: "Barlow Semi Condensed", sans-serif;
    text-align: center; line-height: 1;
  }
  .company__name {
    font-weight: 600; font-size: 29px; letter-spacing: 2.6px; color: var(--teal-muted);
  }
  .company__tag {
    margin-top: 7px; font-weight: 400; font-size: 26px; letter-spacing: 3.4px; color: var(--teal-muted);
  }

  .person { position: absolute; left: 33px; top: 200px; font-family: "Montserrat", sans-serif; }
  .person__name { font-weight: 600; font-size: 26px; color: var(--teal); line-height: 1.1; }
  .person__role { font-size: 15px; color: var(--ink); margin-top: 2px; }

  .address {
    position: absolute; left: 38px; top: 268px;
    font-family: "Montserrat", sans-serif; font-size: 16px; line-height: 21px; color: var(--ink);
  }
  .contacts {
    position: absolute; left: 38px; top: 334px; list-style: none;
    font-family: "Montserrat", sans-serif; font-size: 16px; color: var(--ink);
  }
  .contacts li { display: flex; align-items: center; gap: 7px; height: 24.5px; }
  .contacts svg { width: 15px; height: 15px; fill: var(--teal); }

  .brand-mark {
    position: absolute; left: 405px; top: 50px; width: 297px; height: 365px;
    display: flex; flex-direction: column; align-items: center; justify-content: center; gap: 18px;
  }
  .brand-mark__square { width: 56px; height: 56px; background: var(--mark-grey); }
  .brand-mark__name {
    font-family: "Barlow Semi Condensed", sans-serif; font-weight: 600;
    font-size: 40px; letter-spacing: 2px; color: var(--mark-grey); text-transform: uppercase;
  }

  .pattern-field {
    position: absolute; inset: 0;
    background: linear-gradient(100deg, var(--silver) 0%, #6d6d6d 30%, #2b2b2b 60%, var(--shade) 100%);
    opacity: .55;
  }
</style>
</head>
<body>
<main class="canvas">
  <section class="card card--front" aria-label="Card front">
    <div class="company">
      <div class="company__name">HARBOURLINE SUITES</div>
      <div class="company__tag">RESIDENCES</div>
    </div>

    <div class="person">
      <div class="person__name">Daniel Reyes</div>
      <div class="person__role">owner</div>
    </div>

    <address class="address" style="font-style:normal">
      4820 Cedar Lane, Suite 105<br>
      Lakeview, FL 33019
    </address>

    <ul class="contacts">
      <li>
        <svg viewBox="0 0 16 16" aria-hidden="true"><path d="M2 6c0-2 3-3 6-3s6 1 6 3l-1 1.5-2.5-.8V5.2H5.5v1.5L3 7.5z"/><rect x="3.5" y="8" width="9" height="5" rx="1"/></svg>
        (555) 318-4402
      </li>
      <li>
        <svg viewBox="0 0 16 16" aria-hidden="true"><path d="M1.5 4h13v1.2L8 9 1.5 5.2zM1.5 6.6 8 10.4l6.5-3.8V12h-13z"/></svg>
        hello@samplemail.com
      </li>
      <li>
        <svg viewBox="0 0 16 16" aria-hidden="true"><circle cx="8" cy="8" r="6.5"/></svg>
        www.samplewebsite.com
      </li>
    </ul>

    <div class="brand-mark">
      <div class="brand-mark__square"></div>
      <div class="brand-mark__name">Harbourline</div>
    </div>
  </section>

  <section class="card card--back" aria-label="Card back">
    <div class="pattern-field" role="img" aria-label="Repeating brand pattern fading from silver to black, with one accent in teal"></div>
  </section>
</main>
</body>
</html>
```